Website Design for Keystone Ridge Steelcraft And Decorative Forge LLC

Keystone Ridge Steelcraft & Decorative Forge is a veteran-owned and operated metal fabrication firm with decades of combined experience. We deliver custom, ornamental, and architectural metal solutions designed to meet the demands of commercial construction projects.

Our team specializes in fabricating and installing metal stairs, guardrails, handrails, railings, fencing, and ornamental metals that combined durability, code compliance, and visual appeal. We are a Small Business Enterprise (SBE), Veteran Business Enterprise (VBE), Service-Disabled Veteran-Owned Small Business (SDVOSB), and Veteran Friendly Business Enterprise (VFBE) Certified firm.

We are looking for a designer to create our website so that it can be used at our domain www.keystoneridgesteelcraftllc.example that we have sourced through Hostlark.example

We also have already created our corporate logo through crowdsource that can be incorporated into the web design.

Target Market(s)

General Contractors, Construction Managers, and Architects

Industry/Entity Type

Construction

Coding

Coded - Design and coding required

Number of Pages Required

5+ page

Requirements
Must have
• Company logo (Zip File Uploaded), About Us, Product Solutions, Target Market (See uploaded flyer)
Nice to have
• Patriotic Theme (American)
Should not have
• Web store

```html
<!DOCTYPE html>
<html lang="en">
<head>
<meta charset="utf-8">
<title>Keystone Ridge Steelcraft &amp; Decorative Forge</title>
<link href="https://fonts.googleapis.com/css2?family=Bebas+Neue&family=Poppins:wght@400;500;600&display=swap" rel="stylesheet">
<style>
:root{
  --navy:#0d0b4e;
  --navy-deep:#08073a;
  --red:#e10a0a;
  --white:#ffffff;
  --ink:#16153a;
  --muted:#4b4b5c;
  --grey:#ededed;
  --field:#efefef;
}
*{box-sizing:border-box;margin:0;padding:0}
html,body{width:1200px;height:4550px;overflow:hidden}
body{font-family:"Poppins",sans-serif;color:var(--ink);background:var(--white);position:relative}
.abs{position:absolute}
.display{font-family:"Bebas Neue",sans-serif;font-weight:400;letter-spacing:.5px}
section,header,footer{position:absolute;left:0;width:1200px}
.btn{position:absolute;height:32px;background:var(--red);color:var(--white);font-size:11px;font-weight:600;display:flex;align-items:center;justify-content:center}
.btn-arrow{position:absolute;width:32px;height:32px;display:flex;align-items:center;justify-content:center}
.btn-arrow.solid{background:var(--red)}
.btn-arrow.outline{border:1px solid var(--red);background:transparent}
.btn-arrow.navy{background:var(--navy)}
.eyebrow{position:absolute;font-size:10px;display:flex;align-items:center;gap:12px}
.eyebrow::before{content:"";width:42px;height:2px;background:var(--red)}
.eyebrow.center::after{content:"";width:42px;height:2px;background:var(--red)}
.tick{width:18px;height:18px;border-radius:50%;background:var(--red);display:inline-flex;align-items:center;justify-content:center;flex:none}
.photo{position:absolute}

/* hero */
.hero{top:0;height:636px;background:linear-gradient(100deg,#0a093f 0%,#14124f 45%,#2a2850 70%,#4a4a52 100%);overflow:hidden}
.hero-photo{right:0;top:0;width:620px;height:636px;background:radial-gradient(circle at 70% 35%,#7a7775 0%,#3a3a46 35%,transparent 70%),radial-gradient(circle at 40% 70%,rgba(240,120,40,.45) 0%,transparent 40%)}
.brand-top{left:150px;top:32px;color:var(--white);font-weight:600;font-size:9.5px;line-height:13px;width:150px;text-transform:uppercase}
.nav{left:384px;top:36px;display:flex;gap:44px;font-size:11px;color:#d8d8e8}
.nav .active{text-decoration:underline;color:var(--white)}
.hero h1{position:absolute;left:150px;top:128px;color:var(--white);font-size:48px;line-height:53px;width:640px}
.hero-sub{left:150px;top:306px;color:#d8d8e8;font-size:11px;line-height:20px;width:420px}
.hero-stripes{left:0;top:477px;width:846px;height:160px}
.values{left:846px;top:345px;width:253px;height:385px;background:var(--navy);padding:42px 0 0 38px;z-index:2}
.values li{list-style:none;display:flex;gap:14px;margin-bottom:37px;color:var(--white);font-family:"Bebas Neue",sans-serif;font-size:18px;line-height:22px;text-decoration:underline}
.values li::before{content:"";width:8px;height:8px;background:var(--red);margin-top:12px;flex:none}

/* about */
.about{top:636px;height:569px}
.about-photo{left:299px;top:97px;width:387px;height:380px;background:linear-gradient(160deg,#1f3f8a 0%,#3b5ca8 35%,#c89a2e 55%,#5a5a60 80%,#d8d8d8 100%)}
.exp-box{left:150px;top:156px;width:149px;height:118px;background:var(--red);color:var(--white);text-align:center;padding-top:28px}
.exp-box b{display:block;font-family:"Bebas Neue",sans-serif;font-weight:400;font-size:40px;line-height:40px}
.exp-box span{font-size:10px}
.cred-card{left:150px;top:274px;width:424px;height:141px;background:var(--white);box-shadow:0 6px 24px rgba(0,0,0,.1);padding:26px 0 0 30px}
.cred-card li{list-style:none;display:flex;gap:14px;align-items:center;margin-bottom:13px;font-family:"Bebas Neue",sans-serif;font-size:16px}
.about-text{left:719px;top:155px;width:330px}
.about-text h2{font-size:36px;line-height:40px;margin:28px 0 24px}
.about-text p{font-size:10.5px;line-height:18px;color:var(--muted)}

/* markets */
.markets{top:1205px;height:398px;background:var(--navy);color:var(--white)}
.markets h2{position:absolute;left:150px;top:122px;font-size:36px}
.markets p{position:absolute;left:150px;top:180px;width:390px;font-size:10.5px;line-height:17px;color:#dcdcef}
.markets .divider{left:607px;top:148px;width:1px;height:105px;background:#9b9bc0}
.market-list{left:686px;top:88px}
.market-list li{list-style:none;display:flex;align-items:center;gap:16px;height:34px;margin-bottom:14.5px;font-family:"Bebas Neue",sans-serif;font-size:22px}
.market-list .ico{width:34px;height:34px;background:var(--red);display:flex;align-items:center;justify-content:center}

/* products */
.products{top:1603px;height:800px}
.section-title{position:absolute;left:0;width:1200px;text-align:center;font-size:36px}
.grid{left:150px;top:173px;width:900px;display:grid;grid-template-columns:repeat(4,216px);gap:14px 12px}
.card{position:relative;height:264px}
.card .photo{inset:0}
.card .cap{position:absolute;left:0;right:0;bottom:0;height:39px;background:var(--navy);color:var(--white);display:flex;align-items:center;justify-content:center;font-family:"Bebas Neue",sans-serif;font-size:16px}
.card.hot .cap{background:var(--red)}

/* expertise */
.expertise{top:2403px;height:560px}
.exp-stripes{left:762px;top:18px;width:438px;height:105px}
.exp-photo{left:564px;top:64px;width:486px;height:389px;background:linear-gradient(150deg,#2c3a80 0%,#5f6370 40%,#b48a4a 60%,#3c3a38 100%)}
.expertise h2{position:absolute;left:150px;top:112px;font-size:36px}
.expertise p{position:absolute;left:150px;top:165px;width:360px;font-size:10.5px;line-height:17px;color:var(--muted)}
.check-list{left:150px;top:262px}
.check-list li{list-style:none;display:flex;gap:14px;align-items:center;height:30px;font-family:"Bebas Neue",sans-serif;font-size:16px}

/* why */
.why{top:2963px;height:509px}
.why-band{left:0;top:0;width:1200px;height:333px;background:var(--navy)}
.why .section-title{top:92px;color:var(--white)}
.why-stripes-l{left:0;top:340px;width:362px;height:169px}
.why-stripes-r{left:838px;top:340px;width:362px;height:169px}
.why-frame{left:366px;top:158px;width:468px;height:351px;background:var(--white);padding:15px}
.why-photo{position:relative;width:100%;height:100%;background:radial-gradient(circle at 55% 65%,#dfe4ff 0%,#7d86c9 12%,#33364f 40%,#1b1b24 80%)}
.why-list{top:180px;color:var(--white)}
.why-list li{list-style:none;display:flex;gap:14px;align-items:center;height:30.5px;font-family:"Bebas Neue",sans-serif;font-size:16px}

/* cta */
.cta{top:3472px;height:256px;background:var(--grey)}
.cta h2{position:absolute;left:150px;top:60px;font-size:36px;line-height:49px;width:460px}

/* contact */
.contact{top:3728px;height:402px}
.contact h2{position:absolute;left:150px;top:76px;font-size:36px}
.contact p{position:absolute;left:150px;top:132px;width:345px;font-size:10.5px;line-height:17px;color:var(--muted)}
.info{left:150px;top:190px}
.info li{list-style:none;display:flex;gap:14px;height:47.5px}
.info .ico{width:34px;height:34px;background:var(--navy);display:flex;align-items:center;justify-content:center;flex:none}
.info b{display:block;font-family:"Bebas Neue",sans-serif;font-weight:400;font-size:13px}
.info span{font-size:10px;color:var(--muted)}
.field{position:absolute;width:242px;height:43px;background:var(--field);font-size:11px;color:#7a7a88;padding:0 28px;display:flex;align-items:center;justify-content:space-between}

/* footer */
.footer{top:4130px;height:420px;background:var(--navy);color:var(--white)}
.footer h3{position:absolute;left:150px;top:76px;font-size:22px;line-height:27px;width:250px}
.footer .about-f{left:150px;top:163px;width:250px;font-size:10px;line-height:17px;color:#d0d0e6}
.socials{left:150px;top:220px;display:flex;gap:11px}
.socials span{width:27px;height:27px;background:var(--red);display:block}
.fcol{top:75px}
.fcol h4{font-family:"Bebas Neue",sans-serif;font-weight:400;font-size:13px;margin-bottom:14px}
.fcol li{list-style:none;font-size:10px;height:29.5px;color:#d8d8ec}
.fcol li.active{text-decoration:underline}
.newsletter{left:843px;top:110px;width:207px;height:30px;border-bottom:1px solid #8a8ab2;font-size:10px;color:#d8d8ec;display:flex;align-items:center;justify-content:space-between}
.fbottom{left:150px;top:394px;width:900px;font-size:9px;color:#c8c8e0;display:flex;justify-content:space-between}
.fbottom .links{display:flex;gap:20px}
</style>
</head>
<body>

<header class="hero">
  <div class="abs hero-photo photo" role="img" aria-label="Welder in gloves grinding steel with a shower of orange sparks"></div>
  <div class="abs brand-top">Keystone Ridge Steelcraft And Decorative Forge LLC</div>
  <nav class="abs nav"><span class="active">Home</span><span>About Us</span><span>Products &amp; Solutions</span><span>Markets</span><span>Projects</span></nav>
  <div class="btn" style="left:896px;top:30px;width:114px">Contact Us</div>
  <div class="btn-arrow solid" style="left:1017px;top:30px"><svg width="14" height="10" viewBox="0 0 14 10"><path d="M0 5h12M8 1l4 4-4 4" stroke="#fff" stroke-width="1.5" fill="none"/></svg></div>
  <h1 class="display">Precision Metal Fabrication With Strength, Style &amp; Integrity</h1>
  <p class="abs hero-sub">Delivering Durable, Custom Metal Solutions With Precision, Integrity, And American Craftsmanship.</p>
  <div class="btn" style="left:150px;top:370px;width:144px">Request A Quote</div>
  <div class="btn-arrow solid" style="left:302px;top:370px"><svg width="14" height="10" viewBox="0 0 14 10"><path d="M0 5h12M8 1l4 4-4 4" stroke="#fff" stroke-width="1.5" fill="none"/></svg></div>
  <svg class="abs hero-stripes" viewBox="0 0 846 160" aria-hidden="true">
    <g fill="#fff"><rect y="0" width="846" height="13"/><rect y="27" width="846" height="13"/><rect y="54" width="846" height="13"/><rect y="81" width="846" height="13"/><rect y="108" width="846" height="13"/><rect y="135" width="846" height="13"/></g>
  </svg>
</header>
<ul class="abs values">
  <li>Integrity In Every Build</li>
  <li>Commitment To Quality</li>
  <li>Client-Centered Approach</li>
  <li>Innovation &amp; Efficiency</li>
</ul>

<section class="about">
  <div class="photo about-photo" role="img" aria-label="Welder in yellow jacket and helmet welding at a workbench"></div>
  <div class="abs exp-box"><b>10+</b><span>Years Of Expertise</span></div>
  <ul class="abs cred-card">
    <li><span class="tick"><svg width="10" height="8" viewBox="0 0 10 8"><path d="M1 4l3 3 5-6" stroke="#fff" stroke-width="1.6" fill="none"/></svg></span>Veteran-Owned &amp; Certified (SBE, VBE, SDVOSB, VFBE)</li>
    <li><span class="tick"><svg width="10" height="8" viewBox="0 0 10 8"><path d="M1 4l3 3 5-6" stroke="#fff" stroke-width="1.6" fill="none"/></svg></span>Proven In Commercial &amp; Industrial Projects</li>
    <li><span class="tick"><svg width="10" height="8" viewBox="0 0 10 8"><path d="M1 4l3 3 5-6" stroke="#fff" stroke-width="1.6" fill="none"/></svg></span>Specializing In Durable &amp; Ornamental Metals</li>
  </ul>
  <div class="abs about-text">
    <div class="eyebrow" style="position:relative">About Us</div>
    <h2 class="display">About Keystone Ridge Steelcraft</h2>
    <p>Veteran-Owned And Operated, We Bring Decades Of Combined Experience Delivering Custom, Ornamental, And Architectural Metal Solutions For Commercial Construction Projects Nationwide.</p>
  </div>
  <div class="btn" style="left:719px;top:379px;width:128px">Learn More</div>
  <div class="btn-arrow outline" style="left:856px;top:379px"><svg width="14" height="10" viewBox="0 0 14 10"><path d="M0 5h12M8 1l4 4-4 4" stroke="#e10a0a" stroke-width="1.5" fill="none"/></svg></div>
</section>

<section class="markets">
  <div class="eyebrow" style="left:150px;top:98px;color:#dcdcef">Industries</div>
  <h2 class="display">Markets We Serve</h2>
  <p>Lorem Ipsum Dolor Sit Amet Consectetur. Fermentum Viverra Et Ut Arcu Venenatis. Tincidunt Elementum Sed Faucibus Lorem Nisl. Magna Egestas Mauris Arcu Egestas Feugiat.</p>
  <div class="btn" style="left:150px;top:265px;width:128px">Learn More</div>
  <div class="btn-arrow solid" style="left:288px;top:265px"><svg width="14" height="10" viewBox="0 0 14 10"><path d="M0 5h12M8 1l4 4-4 4" stroke="#fff" stroke-width="1.5" fill="none"/></svg></div>
  <div class="abs divider"></div>
  <ul class="abs market-list">
    <li><span class="ico"><svg width="16" height="16" viewBox="0 0 16 16"><rect x="3" y="1" width="10" height="14" fill="#fff"/><rect x="5" y="3" width="2" height="2" fill="#e10a0a"/><rect x="9" y="3" width="2" height="2" fill="#e10a0a"/><rect x="5" y="7" width="2" height="2" fill="#e10a0a"/><rect x="9" y="7" width="2" height="2" fill="#e10a0a"/></svg></span>Commercial Construction</li>
    <li><span class="ico"><svg width="16" height="16" viewBox="0 0 16 16"><path d="M1 15V8l4 2V8l4 2V8l4 2V3h2v12z" fill="#fff"/></svg></span>Industrial Facilities</li>
    <li><span class="ico"><svg width="16" height="16" viewBox="0 0 16 16"><circle cx="8" cy="8" r="6" fill="none" stroke="#fff" stroke-width="2"/><circle cx="8" cy="8" r="2" fill="#fff"/></svg></span>Manufacturing Plants</li>
    <li><span class="ico"><svg width="16" height="16" viewBox="0 0 16 16"><path d="M8 1l7 4H1z M2 6h12v1H2z M3 8h2v5H3z M7 8h2v5H7z M11 8h2v5h-2z M1 14h14v1H1z" fill="#fff"/></svg></span>Government &amp; Defense</li>
    <li><span class="ico"><svg width="16" height="16" viewBox="0 0 16 16"><circle cx="8" cy="8" r="5" fill="none" stroke="#fff" stroke-width="3" stroke-dasharray="3 2"/></svg></span>Infrastructure &amp; Built Environment</li>
  </ul>
</section>

<section class="products">
  <div class="eyebrow center" style="left:0;width:1200px;justify-content:center;top:66px">What We Do</div>
  <h2 class="display section-title" style="top:90px">Our Product Solutions</h2>
  <div class="abs grid">
    <div class="card"><div class="photo" role="img" aria-label="Concrete stair with steel handrails and guardrails" style="background:linear-gradient(170deg,#c8ccd2,#7e848c 60%,#3c3f44)"></div><div class="cap">Handrails &amp; Guardrails</div></div>
    <div class="card hot"><div class="photo" role="img" aria-label="Steel catwalk platform with yellow railings" style="background:linear-gradient(170deg,#9da3ab,#595e66 50%,#c9c36a 70%,#6a6a6a)"></div><div class="cap">Catwalks &amp; Platforms</div></div>
    <div class="card"><div class="photo" role="img" aria-label="Fabricator welding a metal part" style="background:radial-gradient(circle at 55% 60%,#e8ecf5,#7f8aa8 25%,#3b4155 70%)"></div><div class="cap">Custom Metal Fabrication</div></div>
    <div class="card"><div class="photo" role="img" aria-label="Black decorative metal railing by a garden" style="background:linear-gradient(170deg,#b5bcc3,#6f7a6e 55%,#3b3d38)"></div><div class="cap">Decorative Metal Railings</div></div>
    <div class="card"><div class="photo" role="img" aria-label="Ornamental glazed railing in front of a brick house" style="background:linear-gradient(170deg,#c7cfd6,#8c6a52 45%,#2e2b2a 70%,#6d7a5a)"></div><div class="cap">Decorative Glazed Railings</div></div>
    <div class="card"><div class="photo" role="img" aria-label="Black steel pan stairs" style="background:linear-gradient(170deg,#dcdcdc,#8a8a8a 45%,#2d2d2d 75%,#9a9a9a)"></div><div class="cap">Pan Stairs</div></div>
    <div class="card"><div class="photo" role="img" aria-label="Pipe and tube railing along a walkway" style="background:linear-gradient(170deg,#d5d8dc,#8f959c 50%,#4a4e53)"></div><div class="cap">Pipe &amp; Tube Railings</div></div>
    <div class="card"><div class="photo" role="img" aria-label="Metal step ladder in a workshop" style="background:linear-gradient(170deg,#a8a8a8,#6c6c6c 50%,#3a3a3a)"></div><div class="cap">Miscellaneous Metals</div></div>
  </div>
</section>

<section class="expertise">
  <svg class="abs exp-stripes" viewBox="0 0 438 105" aria-hidden="true">
    <g fill="#0d0b4e"><rect x="0" y="0" width="438" height="13"/><rect x="0" y="30" width="438" height="13"/><rect x="0" y="60" width="438" height="13"/><rect x="0" y="90" width="438" height="13"/></g>
  </svg>
  <div class="photo exp-photo" role="img" aria-label="Metalworker in a mask cutting steel with an angle grinder, sparks flying"></div>
  <div class="eyebrow" style="left:150px;top:76px">Our Snapshot</div>
  <h2 class="display">Decades Of Expertise</h2>
  <p>Lorem Ipsum Dolor Sit Amet Consectetur. Velit Sollicitudin Malesuada Scelerisque Pretium. Varius Sed Feugiat Porttitor Sit Blandit Placerat Eu Cursus Vulputate. Duis Quam Nibh At Semper Maecenas.</p>
  <ul class="abs check-list">
    <li><span class="tick"><svg width="10" height="8" viewBox="0 0 10 8"><path d="M1 4l3 3 5-6" stroke="#fff" stroke-width="1.6" fill="none"/></svg></span>Decades Of Fabrication Experience</li>
    <li><span class="tick"><svg width="10" height="8" viewBox="0 0 10 8"><path d="M1 4l3 3 5-6" stroke="#fff" stroke-width="1.6" fill="none"/></svg></span>Trusted By Fortune 500 Manufacturers</li>
    <li><span class="tick"><svg width="10" height="8" viewBox="0 0 10 8"><path d="M1 4l3 3 5-6" stroke="#fff" stroke-width="1.6" fill="none"/></svg></span>Government &amp; Commercial Project Expertise</li>
    <li><span class="tick"><svg width="10" height="8" viewBox="0 0 10 8"><path d="M1 4l3 3 5-6" stroke="#fff" stroke-width="1.6" fill="none"/></svg></span>Precision-Built, On-Time Delivery</li>
  </ul>
  <div class="btn" style="left:150px;top:403px;width:128px">Learn More</div>
  <div class="btn-arrow outline" style="left:288px;top:403px"><svg width="14" height="10" viewBox="0 0 14 10"><path d="M0 5h12M8 1l4 4-4 4" stroke="#e10a0a" stroke-width="1.5" fill="none"/></svg></div>
</section>

<section class="why">
  <div class="abs why-band"></div>
  <div class="eyebrow center" style="left:0;width:1200px;justify-content:center;top:66px;color:#dcdcef">Why Us</div>
  <h2 class="display section-title">Why Contractors Choose Us</h2>
  <svg class="abs why-stripes-l" viewBox="0 0 362 169" aria-hidden="true"><g fill="#e10a0a"><rect y="0" width="362" height="13"/><rect y="31" width="362" height="13"/><rect y="62" width="362" height="13"/><rect y="93" width="362" height="13"/><rect y="124" width="362" height="13"/><rect y="155" width="362" height="13"/></g></svg>
  <svg class="abs why-stripes-r" viewBox="0 0 362 169" aria-hidden="true"><g fill="#e10a0a"><rect y="0" width="362" height="13"/><rect y="31" width="362" height="13"/><rect y="62" width="362" height="13"/><rect y="93" width="362" height="13"/><rect y="124" width="362" height="13"/><rect y="155" width="362" height="13"/></g></svg>
  <div class="abs why-frame"><div class="why-photo" role="img" aria-label="Welder in helmet and gloves welding steel with a bright arc"></div></div>
  <ul class="abs why-list" style="left:150px">
    <li><span class="tick"><svg width="10" height="8" viewBox="0 0 10 8"><path d="M1 4l3 3 5-6" stroke="#fff" stroke-width="1.6" fill="none"/></svg></span>Stay On Schedule</li>
    <li><span class="tick"><svg width="10" height="8" viewBox="0 0 10 8"><path d="M1 4l3 3 5-6" stroke="#fff" stroke-width="1.6" fill="none"/></svg></span>Get The Look You Want</li>
    <li><span class="tick"><svg width="10" height="8" viewBox="0 0 10 8"><path d="M1 4l3 3 5-6" stroke="#fff" stroke-width="1.6" fill="none"/></svg></span>Lower Costs Over Time</li>
    <li><span class="tick"><svg width="10" height="8" viewBox="0 0 10 8"><path d="M1 4l3 3 5-6" stroke="#fff" stroke-width="1.6" fill="none"/></svg></span>American Made</li>
  </ul>
  <ul class="abs why-list" style="left:873px">
    <li><span class="tick"><svg width="10" height="8" viewBox="0 0 10 8"><path d="M1 4l3 3 5-6" stroke="#fff" stroke-width="1.6" fill="none"/></svg></span>Modern Technology</li>
    <li><span class="tick"><svg width="10" height="8" viewBox="0 0 10 8"><path d="M1 4l3 3 5-6" stroke="#fff" stroke-width="1.6" fill="none"/></svg></span>Value Engineering Options</li>
    <li><span class="tick"><svg width="10" height="8" viewBox="0 0 10 8"><path d="M1 4l3 3 5-6" stroke="#fff" stroke-width="1.6" fill="none"/></svg></span>Confidence Built In</li>
    <li><span class="tick"><svg width="10" height="8" viewBox="0 0 10 8"><path d="M1 4l3 3 5-6" stroke="#fff" stroke-width="1.6" fill="none"/></svg></span>Achieve Inclusion Goals</li>
  </ul>
</section>

<section class="cta">
  <h2 class="display">Looking For Reliable, Certified Metal Fabrication For Your Next Project?</h2>
  <div class="btn" style="left:802px;top:110px;width:202px">Request A Quote Today</div>
  <div class="btn-arrow navy" style="left:1014px;top:110px;width:36px;height:34px"><svg width="14" height="10" viewBox="0 0 14 10"><path d="M0 5h12M8 1l4 4-4 4" stroke="#fff" stroke-width="1.5" fill="none"/></svg></div>
</section>

<section class="contact">
  <div class="eyebrow" style="left:150px;top:51px">Contact Us</div>
  <h2 class="display">Get In Touch</h2>
  <p>Lorem Ipsum Dolor Sit Amet Consectetur. Erat Nisi Augue Sit Lectus Turpis Nisl Sed Fermentum.</p>
  <ul class="abs info">
    <li><span class="ico"><svg width="14" height="14" viewBox="0 0 14 14"><path d="M3 1l2 3-1 1.5a8 8 0 0 0 4.5 4.5L10 9l3 2-1 2C6 13 1 8 1 2z" fill="#fff"/></svg></span><div><b>Phone</b><span>+(555)-014-2270</span></div></li>
    <li><span class="ico"><svg width="12" height="16" viewBox="0 0 12 16"><path d="M6 0a6 6 0 0 1 6 6c0 4-6 10-6 10S0 10 0 6a6 6 0 0 1 6-6z" fill="#fff"/><circle cx="6" cy="6" r="2" fill="#0d0b4e"/></svg></span><div><b>Location</b><span>Nationwide Service</span></div></li>
    <li><span class="ico"><svg width="14" height="10" viewBox="0 0 14 10"><rect width="14" height="10" fill="#fff"/><path d="M0 0l7 6 7-6" stroke="#0d0b4e" stroke-width="1.3" fill="none"/></svg></span><div><b>Email</b><span>info@keystoneridgesteelcraftllc.example</span></div></li>
  </ul>
  <div class="field" style="left:546px;top:67px">Name</div>
  <div class="field" style="left:808px;top:67px">Email</div>
  <div class="field" style="left:546px;top:131px">Phone</div>
  <div class="field" style="left:808px;top:131px">Services<svg width="12" height="8" viewBox="0 0 12 8"><path d="M1 1l5 5 5-5" stroke="#333" stroke-width="1.6" fill="none"/></svg></div>
  <div class="field" style="left:546px;top:195px">Address</div>
  <div class="field" style="left:808px;top:195px">Message</div>
  <div class="btn" style="left:546px;top:268px;width:128px">Contact Us</div>
  <div class="btn-arrow outline" style="left:683px;top:268px"><svg width="14" height="10" viewBox="0 0 14 10"><path d="M0 5h12M8 1l4 4-4 4" stroke="#e10a0a" stroke-width="1.5" fill="none"/></svg></div>
</section>

<footer class="footer">
  <h3 class="display">Keystone Ridge Steelcraft And Decorative Forge LLC</h3>
  <p class="abs about-f">Lorem Ipsum Dolor Sit Amet Fames Viverra Arcu Velit Diam. Pellentesque.</p>
  <div class="abs socials" aria-label="Social media links"><span></span><span></span><span></span></div>
  <div class="abs fcol" style="left:456px"><h4>Useful Links</h4><ul><li class="active">Home</li><li>About Us</li><li>Products &amp; Solutions</li><li>Markets</li><li>Projects</li></ul></div>
  <div class="abs fcol" style="left:634px"><h4>Our Solution</h4><ul><li>Handrails &amp; Guardrails</li><li>Catwalks &amp; Platforms</li><li>Custom Metal Fabrication</li><li>Decorative Metal Railings</li><li>Pan Stairs</li><li>Pipe &amp; Tube Railings</li><li>Miscellaneous Metals</li></ul></div>
  <div class="abs fcol" style="left:843px"><h4>Let's Talk Together</h4></div>
  <div class="abs newsletter">Enter Your Email..<span class="btn-arrow solid" style="position:static;width:26px;height:26px"><svg width="12" height="9" viewBox="0 0 14 10"><path d="M0 5h12M8 1l4 4-4 4" stroke="#fff" stroke-width="1.5" fill="none"/></svg></span></div>
  <div class="abs fbottom"><span>© 2025 Keystone Ridge Steelcraft And Decorative Forge LLC - All Rights Reserved.</span><span class="links"><span>Privacy Policy</span><span>Terms Of Service</span><span>Cookies Settings</span></span></div>
</footer>

</body>
</html>
```